Telecom ISP Business Cards and Stationary
Wireless Internet Service Provider
Telecom ISP Business Cards and Stationary - Telecommunications
Creative Brief
Bright & Fun-filled
Leopold Hartvig
Network Manager
4176 Coralwood Ridge Rd. Ste 240 Henderson, NV 89114
leopold@skylornnet.example
www.skylornnet.example

```html
<!DOCTYPE html>
<html lang="en">
<head>
<meta charset="utf-8">
<title>Skylornnet Stationery</title>
<link rel="stylesheet" href="https://fonts.googleapis.com/css2?family=Montserrat:wght@400;600;800&display=swap">
<style>
:root{
  --board:#8c8d90;
  --board-dark:#77787b;
  --navy:#1b1e4a;
  --green:#a9c83b;
  --paper:#ffffff;
  --pocket-shade:#f1f2f4;
  --ink:#2b2d3a;
  --faint:#e9ecf3;
  --rule:#c9ccd6;
}
*{box-sizing:border-box;margin:0;padding:0}
html,body{width:1200px;height:490px;overflow:hidden}
body{font-family:"Montserrat",sans-serif;color:var(--ink)}
.board{position:relative;width:1200px;height:490px;background:radial-gradient(ellipse at 50% 40%,var(--board),var(--board-dark));overflow:hidden}
.piece{position:absolute;background:var(--paper);box-shadow:0 2px 6px rgba(0,0,0,.3);overflow:hidden}
.brand{font-weight:800;color:var(--navy);letter-spacing:.04em;white-space:nowrap;display:flex;align-items:center;gap:4px}
.brand .dot{display:inline-block;border-radius:50%;background:var(--green)}
.brand.light{color:var(--paper)}
.watermark{position:absolute;left:0;right:0;text-align:center;font-weight:800;color:var(--faint);letter-spacing:.03em;white-space:nowrap}
.band{position:absolute;right:0;bottom:0;height:6px;width:55%;background:var(--green);clip-path:polygon(12% 0,100% 0,100% 100%,0 100%)}
.band.navy{background:var(--navy);width:45%;bottom:6px;height:3px}
.tiny{font-size:3px;line-height:4.5px;color:#666;white-space:nowrap}

/* folder */
.folder{position:absolute;left:7px;top:24px;width:454px;height:456px}
.folder-shape{position:absolute;inset:0;filter:drop-shadow(0 2px 3px rgba(0,0,0,.3))}
.folder .brand{position:absolute}
/* letterheads */
.letterhead{top:168px;width:197px;height:276px}
.form-table{position:absolute;left:12px;top:42px;width:110px;border-collapse:collapse}
.form-table td{border:.5px solid var(--rule);height:8px;font-size:3px;padding:0 2px;color:#888}
.text-lines{position:absolute;left:12px;right:12px}
.text-lines i{display:block;height:1px;background:#e1e3ea;margin-bottom:5px}
</style>
</head>
<body>
<main class="board">

  <!-- presentation folder, open flat with pockets -->
  <section class="folder">
    <svg class="folder-shape" width="454" height="456" viewBox="0 0 454 456">
      <rect x="0" y="0" width="226" height="305" fill="var(--navy)"/>
      <rect x="226" y="0" width="228" height="305" fill="var(--paper)"/>
      <path d="M0 305 H454 V456 H330 L318 444 H252 L240 456 H214 L202 444 H136 L124 456 H0 Z" fill="var(--paper)"/>
      <path d="M0 305 H454 V330 L436 346 H18 L0 330 Z" fill="var(--pocket-shade)"/>
      <line x1="226" y1="305" x2="226" y2="456" stroke="#dcdde2" stroke-width="1"/>
      <polygon points="376,290 454,282 454,296 368,296" fill="var(--navy)"/>
      <polygon points="362,296 454,296 454,305 352,305" fill="var(--green)"/>
    </svg>
    <div class="brand light" style="left:36px;top:140px;font-size:17px"><span class="dot" style="width:10px;height:10px"></span>SKYLORNNET</div>
    <div class="brand" style="left:266px;top:140px;font-size:17px"><span class="dot" style="width:10px;height:10px"></span>SKYLORNNET</div>
    <div class="brand" style="left:70px;top:408px;font-size:9px"><span class="dot" style="width:6px;height:6px"></span>SKYLORNNET</div>
    <div class="brand" style="left:296px;top:408px;font-size:9px"><span class="dot" style="width:6px;height:6px"></span>SKYLORNNET</div>
  </section>

  <!-- letterhead with form -->
  <section class="piece letterhead" style="left:499px">
    <div class="brand" style="position:absolute;right:12px;top:14px;font-size:8px">SKYLORNNET</div>
    <table class="form-table">
      <tr><td>Name</td><td></td></tr><tr><td>Date</td><td></td></tr>
      <tr><td>Account</td><td></td></tr><tr><td>Service</td><td></td></tr>
      <tr><td>Notes</td><td></td></tr>
    </table>
    <div class="watermark" style="top:142px;font-size:17px">SKYLORNNET</div>
    <div class="tiny" style="position:absolute;left:12px;bottom:12px">4176 Coralwood Ridge Rd. Ste 240 Henderson, NV 89114</div>
    <div class="band"></div>
  </section>

  <!-- letterhead -->
  <section class="piece letterhead" style="left:710px">
    <div class="brand" style="position:absolute;right:12px;top:14px;font-size:8px">SKYLORNNET</div>
    <div class="text-lines" style="top:48px"><i></i><i></i><i></i><i style="width:70%"></i></div>
    <div class="watermark" style="top:142px;font-size:17px">SKYLORNNET</div>
    <div class="tiny" style="position:absolute;left:12px;bottom:12px">www.skylornnet.example · leopold@skylornnet.example</div>
    <div class="band"></div>
  </section>

  <!-- compliment slip -->
  <section class="piece" style="left:629px;top:108px;width:84px;height:41px">
    <div class="brand" style="position:absolute;left:6px;top:7px;font-size:6px">SKYLORNNET</div>
    <div class="tiny" style="position:absolute;left:6px;top:17px">With compliments<br>Leopold Hartvig</div>
    <div class="band" style="height:3px"></div>
  </section>

  <!-- note pad -->
  <section class="piece" style="left:763px;top:36px;width:87px;height:113px">
    <div class="brand" style="position:absolute;left:8px;top:8px;font-size:7px">SKYLORNNET</div>
    <div class="watermark" style="top:52px;font-size:8px">SKYLORNNET</div>
    <div class="band" style="height:4px"></div>
  </section>

  <!-- memo card -->
  <section class="piece" style="left:852px;top:53px;width:72px;height:86px">
    <div class="brand" style="position:absolute;left:6px;top:7px;font-size:6px">SKYLORNNET</div>
    <div class="watermark" style="top:40px;font-size:6.5px">SKYLORNNET</div>
    <div class="band" style="height:3px"></div>
  </section>

  <!-- business card front -->
  <section class="piece" style="left:960px;top:29px;width:72px;height:43px">
    <div class="brand" style="position:absolute;left:5px;top:5px;font-size:5px">SKYLORNNET</div>
    <div class="tiny" style="position:absolute;left:5px;top:14px;font-size:2.6px;line-height:3.6px">
      <b style="color:var(--navy)">Leopold Hartvig</b><br>Network Manager<br>leopold@skylornnet.example<br>www.skylornnet.example
    </div>
    <div class="band" style="height:3px"></div>
  </section>

  <!-- business card back -->
  <section class="piece" style="left:960px;top:77px;width:72px;height:48px;background:var(--navy)">
    <div class="brand light" style="position:absolute;left:9px;top:20px;font-size:7px"><span class="dot" style="width:4px;height:4px"></span>SKYLORNNET</div>
  </section>

  <!-- large envelope -->
  <section class="piece" style="left:931px;top:163px;width:197px;height:161px">
    <div class="brand" style="position:absolute;left:10px;top:10px;font-size:7px">SKYLORNNET</div>
    <div class="tiny" style="position:absolute;left:10px;top:20px">4176 Coralwood Ridge Rd. Ste 240<br>Henderson, NV 89114</div>
    <div class="band"></div>
  </section>

  <!-- DL envelope back -->
  <section class="piece" style="left:926px;top:348px;width:202px;height:108px">
    <svg width="202" height="108" viewBox="0 0 202 108" style="position:absolute;inset:0">
      <polygon points="0,0 202,0 101,58" fill="var(--navy)"/>
      <polyline points="0,108 101,52 202,108" fill="none" stroke="#e4e6ec" stroke-width="1"/>
    </svg>
    <div class="tiny" style="position:absolute;left:0;right:0;top:66px;text-align:center">Skylornnet<br>Henderson, NV 89114</div>
  </section>

</main>
</body>
</html>
```